Website Redesign /kleiner Spartensender, hauptsächlich Videos
Zielgruppe
85% Männlich, Alter 30 - 65, technikverliebt
Aufgabenstellung
Neuentwicklung der Video-Website.
Mr.KolvoBox ist der erste und einzige unabhängige Zielgruppen-Sender für Neue Medien, Home Entertainment und Satelliten-Kommunikation.
Mit unseren Sendungen informieren wir interessierte Zuschauer sowie Dienstleister und Unternehmen, die sich den Empfang und die Verbreitung digitaler Medien via Satellit, Internet, Kabel oder Mobil auf die Fahne geschrieben haben.
Umsetzung vermutlich mit Wordpress oder Typo3.

```html
<!DOCTYPE html>
<html lang="de">
<head>
<meta charset="utf-8">
<title>Mr.KolvoBox – Der Multimedia-Kanal</title>
<link rel="stylesheet" href="https://fonts.googleapis.com/css2?family=Arimo:wght@400;700&display=swap">
<style>
:root{
  --backdrop:#858384;
  --panel:#404040;
  --panel-light:#888687;
  --brand-red:#b22528;
  --signal-red:#e8141b;
  --white:#ffffff;
  --text-light:#f2f2f2;
  --text-muted:#b4b4b4;
  --frame:#8a8a8a;
  --black:#000000;
}
*{box-sizing:border-box;margin:0;padding:0}
html,body{width:1200px;height:1148px;overflow:hidden}
body{background:var(--backdrop);font-family:"Arimo",Arial,sans-serif;color:var(--text-light);position:relative}
.abs{position:absolute}
.ad-leaderboard{left:441px;top:28px;width:554px;height:128px;background:var(--brand-red)}
.ad-skyscraper{left:1013px;top:178px;width:168px;height:699px;background:var(--panel)}
.site{left:25px;top:177px;width:969px;height:971px;background:var(--panel)}
.brand{left:50px;top:218px;display:flex;align-items:center;gap:12px}
.brand-dot{width:46px;height:46px;border-radius:50%;background:var(--signal-red)}
.brand-name{font-size:50px;font-weight:700;color:var(--white);letter-spacing:-1px;line-height:1}
.brand-tagline{left:222px;top:272px;font-size:14px;color:var(--text-muted)}
.login{left:630px;top:209px;width:333px;height:62px;background:var(--white)}
.newsletter{left:630px;top:276px;width:333px;height:31px;background:var(--white)}
.field{position:absolute;height:22px;border:1px solid var(--signal-red);color:#444;font-size:13px;padding:3px 5px;background:var(--white)}
.ok-btn{position:absolute;width:40px;height:18px;border-radius:9px;background:var(--panel);color:var(--white);font-size:13px;text-align:center;line-height:18px}
.login-link{position:absolute;font-size:13px;color:var(--signal-red);text-decoration:underline}
.nav{left:52px;top:320px;width:912px;height:37px;background:var(--white);display:flex}
.nav a{display:block;height:37px;line-height:37px;padding:0 15px;font-size:15px;color:var(--signal-red);text-decoration:none;border-right:1px solid var(--brand-red)}
.nav a.active{background:var(--signal-red);color:var(--white);font-weight:700;width:80px;border:none;padding:0;text-align:center}
.nav a.current{background:var(--white);color:#555;border-right:none;width:118px;text-align:center;padding:0;background:#e9e9e9}
.subnav{left:52px;top:357px;width:912px;height:33px;background:var(--backdrop);font-size:15px;padding:6px 15px;color:var(--text-light)}
.subnav a{color:var(--text-light)}
.player{left:52px;top:419px;width:556px;height:357px;background:var(--black)}
.play{left:277px;top:535px}
.teaser-list{left:629px;top:419px;width:334px;height:357px;background:var(--panel-light)}
.teaser{position:absolute;left:15px;width:310px;height:92px}
.teaser-thumb{position:absolute;left:0;top:0;width:147px;height:92px;background:linear-gradient(135deg,#2f3a40,#5c6468 50%,#262c30)}
.teaser-text{position:absolute;left:157px;top:8px;width:155px;font-size:13.5px;line-height:17.5px;color:var(--text-light)}
.teaser-text a{color:#3a3a3a}
.banner{left:52px;top:796px;width:554px;height:82px;background:var(--brand-red);text-align:center;font-size:18px;line-height:22px;padding-top:7px;color:var(--text-light)}
.banner-side{left:629px;top:796px;width:334px;height:81px;background:var(--panel-light)}
.card{top:898px;height:180px;border:1px solid var(--frame)}
.card-one{left:54px;width:214px;padding:14px 13px}
.card-two{left:287px;width:319px}
.card p{font-size:13px;line-height:17.5px;color:var(--text-light)}
.poster{position:absolute;left:10px;top:8px;width:111px;height:162px;background:linear-gradient(180deg,#4a5258,#2a2e32 60%,#1b1d20)}
.card-two p{position:absolute;left:134px;top:15px;width:175px}
.tag{position:absolute;white-space:nowrap;color:var(--text-light)}
.footer{left:30px;top:1092px;width:931px;height:42px;border:1px solid var(--frame);padding:0 16px;display:flex;align-items:center;gap:12px;font-size:14px;font-weight:700}
.bookmark{margin-left:auto;width:130px;height:17px;background:var(--white);border:1px solid #ccc}
</style>
</head>
<body>
<div class="abs ad-leaderboard"></div>
<div class="abs ad-skyscraper"></div>
<div class="abs site"></div>

<div class="abs brand"><span class="brand-dot"></span><span class="brand-name">Mr.KolvoBox</span></div>
<div class="abs brand-tagline">Der Multimedia - Kanal</div>

<div class="abs login">
  <div class="field" style="left:17px;top:11px;width:110px">Benutzername</div>
  <div class="field" style="left:152px;top:11px;width:120px">Password</div>
  <div class="ok-btn" style="left:282px;top:13px">ok</div>
  <span class="login-link" style="left:23px;top:39px">registrieren</span>
  <span class="login-link" style="left:159px;top:39px">Password vergessen?</span>
</div>
<div class="abs newsletter">
  <span style="position:absolute;left:21px;top:7px;font-size:14px;color:#333">Newsletter-Abo</span>
  <div class="field" style="left:152px;top:4px;width:120px">E-Mail</div>
  <div class="ok-btn" style="left:282px;top:6px">ok</div>
</div>

<nav class="abs nav">
  <a class="active">Home</a>
  <a class="current">Community</a>
  <a>Games</a>
  <a>Video</a>
</nav>
<div class="abs subnav"><a>News</a> | <a>Forum</a> | <a>Deins</a></div>

<div class="abs player"></div>
<svg class="abs play" width="108" height="108" viewBox="0 0 108 108" aria-hidden="true">
  <circle cx="54" cy="54" r="50" fill="none" stroke="#fff" stroke-width="4"/>
  <path d="M34 26 L84 54 L34 84 L50 54 Z" fill="#fff"/>
</svg>

<div class="abs teaser-list">
  <div class="teaser" style="top:16px">
    <div class="teaser-thumb" role="img" aria-label="Szenenbild zum Filmtrailer"></div>
    <p class="teaser-text">Carla Wendtner in einem rasanten Agenten-Thriller um Überläufer &amp; Verräter. <a>» mehr</a></p>
  </div>
  <div class="teaser" style="top:129px">
    <div class="teaser-thumb" role="img" aria-label="Szenenbild zum Filmtrailer"></div>
    <p class="teaser-text">Carla Wendtner in einem rasanten Agenten-Thriller um Überläufer &amp; Verräter. <a>» mehr</a></p>
  </div>
  <div class="teaser" style="top:241px">
    <div class="teaser-thumb" role="img" aria-label="Szenenbild zum Filmtrailer"></div>
    <p class="teaser-text">Carla Wendtner in einem rasanten Agenten-Thriller um Überläufer &amp; Verräter. <a>» mehr</a></p>
  </div>
</div>

<div class="abs banner">Banner<br>Banner<br>Banner</div>
<div class="abs banner-side"></div>

<div class="abs card card-one">
  <p>Filmausschnitte, Trailer und Bilder aus den aktuellen und kommenden Topfilmen wie "Mondfall Saga", "Tiefschlaf", "Zauberlehrling 7" und mehr.</p>
</div>
<div class="abs card card-two">
  <div class="poster" role="img" aria-label="Filmplakat"></div>
  <p>Filmausschnitte, Trailer und Bilder aus den aktuellen und kommenden Topfilmen wie "Mondfall Saga", "Tiefschlaf", "Zauberlehrling 7" und mehr.</p>
</div>

<div class="abs tagcloud" style="left:0;top:0">
  <span class="tag" style="left:670px;top:930px;font-size:14px">Tagcloud</span>
  <span class="tag" style="left:744px;top:931px;font-size:8px">Tagcloud</span>
  <span class="tag" style="left:819px;top:941px;font-size:8px">Tagcloud</span>
  <span class="tag" style="left:695px;top:954px;font-size:14px;color:#8c8c8c">Tagcloud</span>
  <span class="tag" style="left:838px;top:955px;font-size:18px;font-weight:700;color:#ee6a6a">Tagcloud</span>
  <span class="tag" style="left:738px;top:974px;font-size:23px;font-weight:700;color:#ee6a6a">Tagcloud</span>
  <span class="tag" style="left:858px;top:992px;font-size:14px">Tagcloud</span>
  <span class="tag" style="left:716px;top:1003px;font-size:14px">Tagcloud</span>
  <span class="tag" style="left:795px;top:1019px;font-size:14px">Tagcloud</span>
</div>

<footer class="abs footer">
  <span>Impressum</span><span>Team</span><span>Jobs</span><span>RSS-Feeds</span>
  <span class="bookmark"></span>
</footer>
</body>
</html>
```